Oil & Gas Consultants need a advertisement

We are advertising in some brochures and need a eye catching advertisement. The ads will be different sizes (some business card sized) and up to a full page ad. We want it clear, crisp and catches the eyes of our viewers. I need the ad to work with different sizes of advertising. We are oil and gas consultants who build gas facilities. We like the dark colors with our logo and want it to pop. Our website is www.tundralinefuel.com for more info on our company.

Target Market(s)

Oil & Gas Companies

Industry/Entity Type

Oil And Gas

Font styles to use
Serif
Sans Serif

Colors

Designer to choose colors to be used in the design.

Requirements
Must have
• our logo, our information how to contact us, what we do

```html
<!DOCTYPE html>
<html lang="en">
<head>
<meta charset="utf-8">
<title>Tundraline Fuel Services – Oil and Gas Facilities Done Right</title>
<link href="https://fonts.googleapis.com/css2?family=Montserrat:wght@400;500;700;800&display=swap" rel="stylesheet">
<style>
  :root {
    --stage: #3a3a3a;
    --band: #2b2b2d;
    --silver: #b9bbc0;
    --ink: #1f1f22;
    --light: #f2f2f2;
    --muted: #d6d6d8;
    --sky-top: #e9d3d8;
    --sky-mid: #c9a2ad;
    --horizon: #6d5a6e;
    --pipe: #8fa2c4;
    --pipe-deep: #2d3c66;
  }
  * { margin: 0; padding: 0; box-sizing: border-box; }
  html, body { width: 1200px; height: 1200px; overflow: hidden; background: var(--stage); }
  body { position: relative; font-family: "Montserrat", Arial, sans-serif; }

  .ad {
    position: absolute; left: 214px; top: 100px;
    width: 773px; height: 999px; overflow: hidden;
  }
  .ad__photo {
    position: absolute; inset: 0;
    background:
      radial-gradient(ellipse 60% 25% at 70% 40%, rgba(240,150,110,.45), transparent 70%),
      linear-gradient(180deg, var(--sky-top) 0%, var(--sky-mid) 30%, var(--horizon) 44%, #b8a3b0 48%, var(--pipe) 58%, var(--pipe-deep) 78%, #3f5486 100%);
  }
  .ad__headline {
    position: absolute; left: 73px; top: 66px;
    font-weight: 800; font-size: 50px; line-height: 52px;
    letter-spacing: 0.5px; color: var(--ink); text-transform: uppercase;
  }
  .ad__band { position: absolute; inset: 0; width: 773px; height: 999px; }

  .brand {
    position: absolute; left: 30px; top: 874px; width: 230px; text-align: center;
    color: var(--light);
  }
  .brand__mark {
    width: 70px; height: 70px; border-radius: 50%;
    background: var(--muted); margin: 0 auto 10px;
  }
  .brand__name { font-weight: 500; font-size: 19px; letter-spacing: 0.3px; line-height: 20px; }
  .brand__sub { font-weight: 500; font-size: 19px; letter-spacing: 0.3px; line-height: 20px; }

  .contact { position: absolute; color: var(--light); }
  .contact__label { font-size: 10px; font-weight: 400; letter-spacing: .5px; line-height: 13px; }
  .contact__value { font-size: 10.5px; font-weight: 700; line-height: 13.5px; }
  .contact--mail { left: 298px; top: 934px; }
  .contact--phone { left: 457px; top: 934px; }
  .contact--email { left: 571px; top: 934px; }
  .contact__rule {
    position: absolute; left: 454px; top: 967px; width: 280px; height: 2px; background: #6b6b6e;
  }
  .contact__web {
    position: absolute; left: 459px; top: 975px;
    font-size: 10.5px; font-weight: 700; color: var(--light);
  }
</style>
</head>
<body>
  <div class="ad">
    <div class="ad__photo" role="img" aria-label="Photograph of steel pipelines on a rack leading toward a blurred refinery with tall stacks at sunset"></div>

    <h1 class="ad__headline">Oil and Gas<br>Facilities<br>Done Right</h1>

    <svg class="ad__band" viewBox="0 0 773 999" aria-hidden="true">
      <path d="M0,800 C160,872 360,915 530,906 C650,900 720,894 773,893 L773,999 L0,999 Z" fill="var(--band)"/>
      <path d="M0,796 C160,868 360,911 530,902 C650,896 720,890 773,889" fill="none" stroke="var(--silver)" stroke-width="4"/>
    </svg>

    <div class="brand">
      <div class="brand__mark"></div>
      <div class="brand__name">TUNDRALINE FUEL</div>
      <div class="brand__sub">SERVICES INC</div>
    </div>

    <div class="contact contact--mail">
      <div class="contact__label">MAIL:</div>
      <div class="contact__value">#420, 318 – 8 Avenue SW<br>Calgary, Alberta<br>T2P 1C4</div>
    </div>
    <div class="contact contact--phone">
      <div class="contact__label">PHONE:</div>
      <div class="contact__value">(403) 555-0147</div>
    </div>
    <div class="contact contact--email">
      <div class="contact__label">EMAIL:</div>
      <div class="contact__value">info@tundralinefuel.com</div>
    </div>
    <div class="contact__rule"></div>
    <div class="contact__web">www.tundralinefuel.com</div>
  </div>
</body>
</html>
```